Meditation for IVF and infertility

I need a flyer inviting IVF patients to join my Meditation class, I would like to offer free meditation to ivf women and for couples this class is free every Thursday night at 5 pm
2465 west halloran blvd suite K Santa Barbara Ca 93274
larkvale-meditation.com for more details

```html
<!DOCTYPE html>
<html lang="en">
<head>
<meta charset="utf-8">
<title>Meditation for Infertility and IVF – Flyer</title>
<link href="https://fonts.googleapis.com/css2?family=Great+Vibes&family=Open+Sans:wght@400&family=Poppins:wght@300;400;600;700;800&display=swap" rel="stylesheet">
<style>
  :root {
    --page-bg: #e9e9ea;
    --ink: #1b1b1f;
    --purple: #7a5a97;
    --lavender: #c9b3e0;
    --lavender-soft: #b89fd1;
    --white: #ffffff;
    --night: #1d1a22;
  }
  * { box-sizing: border-box; margin: 0; padding: 0; }
  html, body { width: 1200px; height: 1000px; overflow: hidden; background: var(--page-bg); }
  .flyer {
    position: absolute; left: 292px; top: 102px;
    width: 617px; height: 798px;
    background: var(--white); overflow: hidden;
    font-family: "Poppins", sans-serif;
    box-shadow: 6px 8px 16px rgba(0,0,0,.22);
  }
  .hero-photo {
    position: absolute; left: 0; top: 0; width: 617px; height: 480px;
    background: linear-gradient(100deg, #2a2530 0%, #3d3845 40%, #6d7076 70%, #9aa4a8 100%);
  }
  .hero-shade {
    position: absolute; left: 0; top: 0; width: 617px; height: 480px;
    background: linear-gradient(90deg, rgba(20,16,26,.75) 0%, rgba(20,16,26,.35) 60%, rgba(20,16,26,0) 100%);
  }
  .brand {
    position: absolute; left: 128px; top: 72px; width: 140px;
    display: flex; align-items: center; gap: 8px;
    color: var(--white); font-size: 15px; font-weight: 400; line-height: 1.15;
  }
  .brand-dot { width: 12px; height: 12px; border-radius: 50%; background: var(--white); flex: none; }
  .welcome {
    position: absolute; left: 0; width: 380px; top: 176px; text-align: center;
    font-family: "Great Vibes", cursive; font-size: 70px; color: var(--lavender); line-height: 1;
  }
  .title {
    position: absolute; left: 0; width: 380px; top: 243px; text-align: center;
    color: var(--white); font-weight: 300; font-size: 35px; line-height: 50px;
  }
  .title-rule { position: absolute; left: 145px; top: 356px; width: 98px; height: 2px; background: var(--white); }
  .host {
    position: absolute; left: 0; width: 380px; top: 374px; text-align: center;
    color: var(--lavender); font-weight: 300; font-size: 25px; line-height: 34px;
  }
  .waves { position: absolute; left: 0; top: 0; }
  .photo-circle { position: absolute; border-radius: 50%; border: 5px solid var(--purple); }
  .photo-circle.class-scene {
    left: 358px; top: 295px; width: 260px; height: 260px;
    background: radial-gradient(circle at 55% 45%, #e7c6d4 0%, #b7a5b4 35%, #8ea0b2 70%, #6fa7c3 100%);
  }
  .photo-circle.teacher {
    left: 282px; top: 385px; width: 156px; height: 156px;
    background: radial-gradient(circle at 50% 60%, #2b2a30 0%, #4d5544 45%, #7b8a66 80%, #a37a86 100%);
  }
  .audience-bar { position: absolute; left: 36px; top: 493px; width: 6px; height: 95px; background: var(--lavender-soft); }
  .audience {
    position: absolute; left: 60px; top: 488px;
    font-weight: 600; font-size: 23px; line-height: 32px; color: var(--ink);
  }
  .free {
    position: absolute; left: 60px; top: 550px; line-height: 46px;
    font-weight: 800; font-size: 35px; color: var(--purple); letter-spacing: .3px;
  }
  .about {
    position: absolute; left: 37px; top: 596px; width: 545px;
    font-family: "Open Sans", sans-serif; font-size: 11.5px; line-height: 16.5px; color: var(--ink);
  }
  .pill {
    position: absolute; background: var(--purple); color: var(--white);
    font-weight: 700; display: flex; align-items: center; justify-content: center;
  }
  .pill.details { left: 414px; top: 660px; width: 166px; height: 28px; font-size: 14px; border-radius: 12px 0 12px 0; }
  .pill.schedule { left: 36px; top: 693px; width: 235px; height: 32px; font-size: 22px; border-radius: 0 16px 16px 0; }
  .time { position: absolute; left: 36px; top: 733px; font-weight: 700; font-size: 23px; line-height: 32px; color: var(--ink); }
  .contacts { position: absolute; right: 37px; top: 698px; list-style: none; }
  .contacts li {
    display: flex; justify-content: flex-end; align-items: center; gap: 12px;
    color: var(--white); font-size: 13px; line-height: 25px; text-align: right;
  }
  .contacts li.address { align-items: flex-start; }
  .contacts li.address span { line-height: 20px; margin-top: 2px; }
  .icon { width: 15px; height: 15px; flex: none; }
  .contacts li.address .icon { margin-top: 5px; }
</style>
</head>
<body>
  <main class="flyer">
    <div class="hero-photo" role="img" aria-label="Photo of a group of women meditating cross-legged in a bright studio"></div>
    <div class="hero-shade"></div>

    <div class="brand"><span class="brand-dot"></span><span>Larkvale Meditation</span></div>

    <div class="welcome">Welcome To</div>
    <h1 class="title">Meditation for<br>Infertility and IVF.</h1>
    <div class="title-rule"></div>
    <div class="host">With Dara Quill</div>

    <svg class="waves" width="617" height="798" viewBox="0 0 617 798" aria-hidden="true">
      <path d="M0 418 C 90 468, 220 478, 330 468 L 617 448 L 617 798 L 0 798 Z" fill="var(--white)"/>
      <path d="M0 418 C 80 466, 200 478, 300 470 C 220 480, 100 470, 0 432 Z" fill="var(--lavender-soft)"/>
      <path d="M0 432 C 100 472, 220 482, 300 470 C 210 492, 90 482, 0 448 Z" fill="var(--purple)" opacity=".85"/>
      <path d="M617 684 L 617 798 L 120 798 C 170 784, 230 760, 290 738 C 380 706, 500 690, 617 684 Z" fill="var(--night)"/>
      <path d="M617 678 C 500 684, 380 700, 286 734 C 226 756, 168 780, 110 798 L 124 798 C 180 782, 236 760, 294 740 C 384 710, 500 692, 617 686 Z" fill="var(--purple)"/>
    </svg>

    <div class="photo-circle class-scene" role="img" aria-label="Photo of a pregnant woman meditating on a yoga mat"></div>
    <div class="photo-circle teacher" role="img" aria-label="Portrait photo of the meditation teacher outdoors"></div>

    <div class="audience-bar"></div>
    <h2 class="audience">IVF WOMEN AND<br>FOR COUPLES</h2>
    <div class="free">THIS CLASS IS FREE</div>
    <p class="about">This class is an opportunity to learn to meditate during a stressful time I will teach meditation techniques and lead a 20 minute meditation . After meditation ,I will offer space for a group chat. a place to share and let go . I underwent several IVF treatments and have experienced the need for group healing . My IVF treatment lead me to meditation.</p>

    <div class="pill details">FOR MORE DETAILS</div>
    <div class="pill schedule">EVERY THURSDAY</div>
    <div class="time">NIGHT AT 5 PM</div>

    <ul class="contacts">
      <li><span>707-555-0142</span>
        <svg class="icon" viewBox="0 0 16 16"><circle cx="8" cy="8" r="8" fill="var(--lavender)"/><path d="M5.2 4.2l1.3-.3.8 1.9-.9.7c.5 1.1 1.3 1.9 2.4 2.4l.7-.9 1.9.8-.3 1.3c-3.4.2-6.1-2.5-5.9-5.9z" fill="var(--night)"/></svg></li>
      <li><span>larkvale-meditation.com</span>
        <svg class="icon" viewBox="0 0 16 16"><circle cx="8" cy="8" r="8" fill="var(--lavender)"/><circle cx="8" cy="8" r="4.2" fill="none" stroke="var(--night)" stroke-width="1"/><path d="M3.8 8h8.4M8 3.8c-1.6 2.6-1.6 5.8 0 8.4M8 3.8c1.6 2.6 1.6 5.8 0 8.4" fill="none" stroke="var(--night)" stroke-width="1"/></svg></li>
      <li class="address"><span>2465 west halloran blvd suite K Santa<br>Barbara Ca 93274</span>
        <svg class="icon" viewBox="0 0 16 16"><circle cx="8" cy="8" r="8" fill="var(--lavender)"/><path d="M8 3.5a3 3 0 0 1 3 3c0 2.2-3 5.8-3 5.8S5 8.7 5 6.5a3 3 0 0 1 3-3z" fill="var(--night)"/><circle cx="8" cy="6.5" r="1.1" fill="var(--lavender)"/></svg></li>
    </ul>
  </main>
</body>
</html>
```